International Food Company needs packaging design for new products

We have a logo for our new business. It is attached. Now we need a packaging design for the products that we will be selling. We are an international wholesale foods company selling foods and herbs that will be certified organic and Non-GMO imported from West Africa. We are just in the process of launching new products. We're looking for a design that is fresh and modern.

Here is a list of items that we are requesting packaging design for.

Baobob Powder-8 oz and 12 oz
Dried Mango- 8 oz
Mango Powder 8 oz and 12 oz

```html
<!DOCTYPE html>
<html lang="en">
<head>
<meta charset="utf-8">
<title>Sunvale Herbs – Organic Powder Labels</title>
<link rel="stylesheet" href="https://fonts.googleapis.com/css2?family=Josefin+Sans:wght@300;400;600&family=Signika:wght@400&display=swap">
<style>
  :root {
    --canvas: #f1f1f1;
    --label-black: #0c0c0c;
    --brand-green: #3dcf8e;
    --accent-orange: #ec8d2c;
    --paper: #ecebe7;
    --ink: #161616;
    --baobab-band: #cfbf98;
    --baobab-band-dark: #b6a57c;
    --mango-band: #f2ae14;
    --mango-band-dark: #e39a0a;
    --baobab-art-a: #d9c7a6;
    --baobab-art-b: #9c8462;
    --mango-art-a: #f6dc4a;
    --mango-art-b: #ef8a3c;
    --badge-green: #3dcf8e;
  }
  * { box-sizing: border-box; margin: 0; padding: 0; }
  html, body {
    width: 1200px; height: 900px; overflow: hidden;
    background: var(--canvas);
  }
  .label-row {
    width: 1200px; height: 900px;
    display: flex; justify-content: center; align-items: center; gap: 140px;
  }
  .label {
    position: relative;
    width: 340px; height: 640px;
    background: var(--label-black);
    overflow: hidden;
    box-shadow: 0 10px 30px rgba(0,0,0,0.15);
  }
  .label--baobab { --band: var(--baobab-band); --band-dark: var(--baobab-band-dark); --art-a: var(--baobab-art-a); --art-b: var(--baobab-art-b); }
  .label--mango { --band: var(--mango-band); --band-dark: var(--mango-band-dark); --art-a: var(--mango-art-a); --art-b: var(--mango-art-b); }

  .brand {
    position: absolute; top: 130px; left: 0; right: 0;
    display: flex; justify-content: center; align-items: center; gap: 12px;
  }
  .brand__dot {
    width: 22px; height: 22px; border-radius: 50%;
    background: var(--accent-orange);
  }
  .brand__name {
    font-family: "Josefin Sans", sans-serif;
    font-weight: 300; font-size: 34px; letter-spacing: 1px;
    color: var(--brand-green);
  }

  .band {
    position: absolute; left: 0; right: 0; top: 248px; height: 130px;
    background: var(--band);
    clip-path: polygon(0 12%, 8% 9%, 15% 13%, 24% 8%, 33% 11%, 41% 7%, 52% 10%, 60% 6%, 70% 10%, 78% 5%, 88% 9%, 100% 4%, 100% 100%, 0 100%);
  }
  .paper {
    position: absolute; left: 0; right: 0; top: 350px; height: 250px;
    background: var(--paper);
    clip-path: polygon(0 8%, 10% 5%, 20% 9%, 30% 4%, 42% 7%, 55% 3%, 66% 6%, 78% 2%, 90% 5%, 100% 3%, 100% 100%, 0 100%);
  }
  .paper-edge {
    position: absolute; left: 0; right: 0; top: 598px; height: 4px;
    background: var(--band-dark);
  }
  .product-name {
    position: absolute; left: 0; right: 0; top: 280px;
    text-align: center; color: var(--ink);
    font-family: "Josefin Sans", sans-serif; font-weight: 400;
  }
  .product-name__kind { display: block; font-size: 20px; letter-spacing: 0.5px; }
  .product-name__title { display: block; font-size: 28px; letter-spacing: 0.5px; margin-top: 2px; }

  .origin {
    position: absolute; left: 0; right: 0; top: 380px;
    text-align: center;
    font-family: "Signika", sans-serif; font-size: 19px; line-height: 1.2;
    color: var(--accent-orange);
  }
  .product-art {
    position: absolute; left: 22px; top: 440px; width: 220px; height: 110px;
    border-radius: 50%;
    background: radial-gradient(ellipse at 40% 45%, var(--art-a) 0%, var(--art-b) 75%, transparent 100%);
    opacity: 0.9;
  }
  .badge {
    position: absolute; right: 20px; top: 470px;
    width: 68px; height: 68px; border-radius: 50%;
    border: 3px solid var(--badge-green);
  }
  .net-weight {
    position: absolute; left: 0; right: 0; top: 562px;
    text-align: center;
    font-family: "Josefin Sans", sans-serif; font-weight: 400; font-size: 19px;
    color: var(--ink);
  }
</style>
</head>
<body>
<main class="label-row">
  <section class="label label--baobab">
    <div class="brand"><span class="brand__dot"></span><span class="brand__name">SUNVALE HERBS</span></div>
    <div class="band"></div>
    <div class="paper"></div>
    <div class="paper-edge"></div>
    <h2 class="product-name"><span class="product-name__kind">ORGANIC</span><span class="product-name__title">BAOBOB POWDER</span></h2>
    <p class="origin">Imported from<br>West Africa</p>
    <div class="product-art" role="img" aria-label="Painted illustration of an opened baobab fruit pod with its pale pulp"></div>
    <div class="badge" role="img" aria-label="Non-GMO certification badge"></div>
    <p class="net-weight">NET WT 8 OZ</p>
  </section>

  <section class="label label--mango">
    <div class="brand"><span class="brand__dot"></span><span class="brand__name">SUNVALE HERBS</span></div>
    <div class="band"></div>
    <div class="paper"></div>
    <div class="paper-edge"></div>
    <h2 class="product-name"><span class="product-name__kind">ORGANIC</span><span class="product-name__title">MANGO POWDER</span></h2>
    <p class="origin">Imported from<br>West Africa</p>
    <div class="product-art" role="img" aria-label="Watercolour illustration of sliced ripe mango pieces"></div>
    <div class="badge" role="img" aria-label="Non-GMO certification badge"></div>
    <p class="net-weight">NET WT 8 OZ</p>
  </section>
</main>
</body>
</html>
```